Wine Bottle Label and Logo Design

Wine label needed for small family winery, Hollow Creek Meadow Wines. Draft logo and palette created but need more work on Logo also.
Would like a simple label that has the HCM logo with space to put the wine varietal on the front.

We have a sustainably farmed vineyard, Pemberly Vineyards, which provides the estate grown fruit. We have recently been profiled in the news for our composting efforts. This links shares that and a bit of our story about Hollow Creek Meadow and the western novelist Ottla Breck that our wine is named after.
https://www.tressonmedia.example/local/soil-renewal-story-from-the-coast-helps-tackle-warming/4821906/.

Website of www.pemberlyvineyards.example also has more background (and we are working an update on this as well as need a HCMWines.example website). The back of the wine label will have the Pemberly Vineyards logo.

We are a verified micro-producer with Keepthesmallgrowers.example and want this logo on the front of label.

Attached are sample labels from prior vintages, color palette, logos, and snippets about Ottla Breck.

The HCM logo attached has reference to a blue line stream on our property and is meant to resemble a cattle brand - simple with reference to the land.

We want the label to be reminiscent of a 1920's era ranch, again with the Ottla Breck theme (see more about her at https://archive.halvercollege.example/digital/collection/breck/search).

Target Market(s)

Wine drinkers, sustainable agriculture

Industry/Entity Type

Wine, agriculture, sustainability

Colors

Designer to choose colors to be used in the design.

Requirements
Must have
• 1920's ranch feel, simple. Include KTSG logo on front label
Nice to have
• Color palette as presented on prior Quiet Ember lable
Should not have
• Anything gilded, pompous, too busy

```html
<!DOCTYPE html>
<html lang="en">
<head>
<meta charset="utf-8">
<title>Hollow Creek Meadow – Front Label</title>
<link rel="stylesheet" href="https://fonts.googleapis.com/css2?family=Pinyon+Script&family=Tinos&display=swap">
<style>
  :root {
    --page: #ffffff;
    --label-paper: #f4f4f2;
    --rule-brown: #4a3a30;
    --frame-brown: #5a463c;
    --ink: #4a3a32;
    --terracotta: #c0704f;
    --art-tone: #9c8073;
    --art-glow: #f2d2ac;
    --badge-dark: #3a3532;
    --badge-gold: #c9a46a;
    --vineyard-green: #8e9a6c;
  }
  html, body {
    margin: 0;
    padding: 0;
    width: 1200px;
    height: 999px;
    overflow: hidden;
    background: var(--page);
  }
  .canvas {
    position: relative;
    width: 1200px;
    height: 999px;
  }
  .label-band {
    position: absolute;
    left: 150px;
    top: 240px;
    width: 900px;
    height: 520px;
    background: var(--label-paper);
  }
  .band-rule {
    position: absolute;
    left: 148px;
    width: 904px;
    height: 4px;
    border-radius: 2px;
    background: var(--rule-brown);
  }
  .band-rule.top { top: 236px; }
  .band-rule.bottom { top: 759px; }

  .front-frame {
    position: absolute;
    left: 0;
    top: 0;
  }
  .hero-art {
    position: absolute;
    left: 266px;
    top: 272px;
    width: 274px;
    height: 128px;
    border-radius: 6px;
    background: radial-gradient(ellipse 28% 70% at 50% 45%, var(--art-tone) 0 60%, transparent 100%),
                linear-gradient(180deg, transparent 40%, var(--art-glow) 100%);
  }
  .brand-name {
    position: absolute;
    left: 190px;
    width: 425px;
    top: 402px;
    margin: 0;
    text-align: center;
    font-family: "Pinyon Script", cursive;
    font-weight: 400;
    font-size: 44px;
    line-height: 52px;
    color: var(--terracotta);
    white-space: nowrap;
  }
  .varietal {
    position: absolute;
    left: 190px;
    width: 425px;
    top: 503px;
    margin: 0;
    text-align: center;
    font-family: "Tinos", serif;
    font-size: 23px;
    line-height: 29px;
    color: var(--ink);
    font-weight: 400;
  }
  .appellation {
    position: absolute;
    left: 190px;
    width: 425px;
    top: 580px;
    text-align: center;
    font-family: "Pinyon Script", cursive;
    font-size: 31px;
    line-height: 38px;
    color: var(--terracotta);
  }
  .vintage {
    position: absolute;
    left: 190px;
    width: 425px;
    top: 623px;
    text-align: center;
    font-family: "Tinos", serif;
    font-size: 25px;
    color: var(--ink);
  }
  .spec {
    position: absolute;
    top: 708px;
    font-family: "Tinos", serif;
    font-size: 18px;
    color: var(--ink);
    white-space: nowrap;
  }
  .spec small { font-size: 15px; }
  .spec.volume { left: 252px; }
  .spec.abv { left: 475px; }
  .grower-badge {
    position: absolute;
    left: 365px;
    top: 670px;
    width: 76px;
    height: 76px;
    border-radius: 50%;
    background: radial-gradient(circle, var(--badge-gold) 0 48%, var(--badge-dark) 50% 100%);
  }

  .estate-mark {
    position: absolute;
    left: 760px;
    top: 486px;
    display: flex;
    align-items: center;
    gap: 10px;
    font-family: "Tinos", serif;
    font-size: 18px;
    color: var(--ink);
    white-space: nowrap;
  }
  .estate-mark .dot {
    width: 22px;
    height: 22px;
    border-radius: 50%;
    background: var(--vineyard-green);
  }
</style>
</head>
<body>
<main class="canvas">
  <div class="label-band"></div>
  <div class="band-rule top"></div>
  <div class="band-rule bottom"></div>

  <svg class="front-frame" width="1200" height="999" viewBox="0 0 1200 999" aria-hidden="true">
    <path d="M210 254 H596 A18 18 0 0 0 614 272 V727 A18 18 0 0 0 596 745 H210 A18 18 0 0 0 192 727 V272 A18 18 0 0 0 210 254 Z" fill="none" stroke="var(--frame-brown)" stroke-width="1.6"/>
  </svg>

  <div class="hero-art" role="img" aria-label="Illustration of a rider on horseback over a sunlit ridge line"></div>
  <h1 class="brand-name">Hollow Creek Meadow</h1>
  <h2 class="varietal">WHITE - FRUITY<br>CABERNET SAUVIGNON</h2>
  <div class="appellation">Hollow Creek</div>
  <div class="vintage">2023</div>
  <div class="spec volume">750 <small>ML</small></div>
  <div class="grower-badge" role="img" aria-label="Verified micro-producer certification badge"></div>
  <div class="spec abv">14% <small>ALC/VOL</small></div>

  <div class="estate-mark"><span class="dot"></span>Pemberly Vineyards</div>
</main>
</body>
</html>
```